Indie Scifi Writer Needs Book Cover for First in Series Space Adventure

I need an ebook cover and print book cover for the first episode in a humorous, action-filled space adventure called Orbit Sleuth. Here's a rough blurb for a flavour of the book:
Twenty-something Mabel Quorridge has not made much of a success of her life, and her ex-boyfriend's accusation that she never pays attention may carry some truth. But all that is about to change when Mabel is sucked into a mysterious green mist that appears beneath her kitchen sink.
Encountering a terrifying insectoid alien sets Mabel on the path to a fast-paced space adventure that tests her concentration, fighting abilities and skills of deduction. The Intersolar Assembly hires her to investigate a conflict between the mechanical placktoids and the mysterious oootoon, a single entity comprising billions in individual personalities.
Drawn into the adventure is Mabel's steady, level-headed work colleague, Nigel, who reveals he has a secret vice and an impulsive nature when pushed too far.
In uncovering the true aggressor in the conflict between the placktoids and oootoon, Mabel and Nigel reveal a threat to the entire galaxy.
Beta readers have described the feel of the book as a cross between Mr.Kettle and Wanderers Almanac of the Cosmos.
There is a space ship in the story, but it's pitch black, so may not be a good fit for the cover. The green mist is central to the series, and my initial thoughts are to have the title in silver and shaped like a space ship, disappearing into a spiral of green mist set against an outer space background - disappearing in a similar way that the Vorbel disappears down its vortex, or the preface words disappear into space at the beginning of Comet Feud.
While the book is humorous, the emphasis for the cover should be the fast-paced space adventure aspect. Branding is important. I'm planning at least four in the series while waiting to see if it gains traction.
The title should read Orbit Sleuth and the subtitle is Episode One: Errand Unlikely. My pen name is P.R. Moss.
Target Market(s)
Science fiction readers
Industry/Entity Type
Detective
Look and feel

```html
<!DOCTYPE html>
<html lang="en">
<head>
<meta charset="utf-8">
<title>Orbit Sleuth — Episode One: Errand Unlikely</title>
<link rel="stylesheet" href="https://fonts.googleapis.com/css2?family=Audiowide&family=Orbitron:wght@500;700&display=swap">
<style>
  :root {
    --space-black: #040605;
    --space-deep: #0c120c;
    --nebula-green: #2f4a26;
    --nebula-moss: #4d6a3a;
    --dust-brown: #5b4a33;
    --core-cream: #cbbf9c;
    --core-glow: #9a8a66;
    --title-fill: #c3eb94;
    --subtitle: #eef4e4;
    --author: #b4dc86;
  }
  * { margin: 0; padding: 0; box-sizing: border-box; }
  html, body {
    width: 802px; height: 1200px; overflow: hidden;
    background: var(--space-black);
  }
  .cover {
    position: relative; width: 802px; height: 1200px; overflow: hidden;
  }
  .cover__starfield {
    position: absolute; inset: 0;
    background:
      radial-gradient(ellipse 150px 230px at 380px 880px, rgba(203,191,156,0.75), transparent 70%),
      radial-gradient(ellipse 210px 150px at 560px 560px, rgba(154,138,102,0.55), transparent 72%),
      radial-gradient(ellipse 260px 200px at 300px 760px, rgba(91,74,51,0.7), transparent 72%),
      radial-gradient(ellipse 240px 190px at 660px 300px, rgba(91,74,51,0.45), transparent 72%),
      radial-gradient(ellipse 300px 260px at 120px 600px, rgba(77,106,58,0.65), transparent 72%),
      radial-gradient(ellipse 280px 220px at 700px 720px, rgba(47,74,38,0.7), transparent 72%),
      radial-gradient(ellipse 260px 200px at 200px 250px, rgba(47,74,38,0.55), transparent 72%),
      radial-gradient(ellipse 320px 240px at 620px 1080px, rgba(47,74,38,0.6), transparent 72%),
      linear-gradient(60deg, transparent 25%, rgba(91,74,51,0.45) 45%, rgba(154,138,102,0.35) 55%, transparent 75%),
      linear-gradient(180deg, var(--space-deep) 0%, var(--space-black) 100%);
  }
  .title {
    position: absolute; left: 0; right: 0; top: 158px;
    text-align: center;
    font-family: "Audiowide", sans-serif;
    font-weight: 400;
    color: var(--title-fill);
    line-height: 1;
    text-transform: uppercase;
  }
  .title__line { display: block; font-size: 118px; }
  .title__line--top { letter-spacing: 2px; }
  .title__line--bottom { letter-spacing: 6px; margin-top: 14px; }
  .subtitle {
    position: absolute; left: 0; right: 0; top: 456px;
    text-align: center;
    font-family: "Orbitron", sans-serif; font-weight: 700;
    font-size: 29px; letter-spacing: 2px;
    color: var(--subtitle);
    text-transform: uppercase;
  }
  .author {
    position: absolute; left: 0; right: 0; top: 976px;
    text-align: center;
    font-family: "Orbitron", sans-serif; font-weight: 500;
    font-size: 80px; letter-spacing: 4px;
    color: var(--author);
  }
</style>
</head>
<body>
<main class="cover">
  <div class="cover__starfield" role="img" aria-label="Starfield photograph: the Milky Way band of green mist, brown dust and a bright cream core crossing the cover, scattered with stars"></div>

  <h1 class="title">
    <span class="title__line title__line--top">Orbit</span>
    <span class="title__line title__line--bottom">Sleuth</span>
  </h1>
  <p class="subtitle">Episode One: Errand Unlikely</p>
  <p class="author">P.R. MOSS</p>
</main>
</body>
</html>
```